Website for IT consulting Company

I need a website upgrade, the existing site content is ok, I would also like to add a testimonial page, the site should be something that is easy for us to update content. You use the content from www.velmarketa.com as an example. I will also post update logo and artwork. I also need a contact form with some type of validation or captcha.

Please omit Address maps

Target Market(s)

small business, service oriented companies. We provide IT Consulting, support and mangement

Industry/Entity Type

Information Technology

Coding

Coded - Design and coding required

Number of Pages Required

1 page

Font styles to use
Serif
Sans Serif

Requirements
Must have
• Contain logo attached, and content from existing web site www.velmarketa.com.
• Also need to update content easily, and be movable to different platforms.
• There is a catch phrase
• "Let us worry about your technology…” “ so you don’t have to!”
• Should be included.
Nice to have
• Testimonial page, Project page where we can post new and past projects and pictures
Should not have
• none

```html
<!DOCTYPE html>
<html lang="en">
<head>
<meta charset="utf-8">
<title>Velmarketa – IT Solutions</title>
<link rel="stylesheet" href="https://fonts.googleapis.com/css2?family=Roboto:wght@400;500;700&family=Roboto+Condensed:wght@700&display=swap">
<style>
:root{
  --orange:#f58220;
  --orange-dark:#e06d10;
  --black:#0d0d0d;
  --ink:#1a1a1a;
  --text:#555;
  --muted:#777;
  --grey-bg:#efefef;
  --white:#fff;
}
*{box-sizing:border-box;margin:0;padding:0}
html,body{width:1200px;height:2936px;overflow:hidden}
body{font-family:"Roboto",Arial,sans-serif;color:var(--ink);background:var(--white)}

/* header */
.site-header{position:absolute;top:0;left:0;width:1200px;height:108px;background:var(--black)}
.brand{position:absolute;left:58px;top:26px;display:flex;align-items:center;gap:10px}
.brand-mark{width:34px;height:34px;background:var(--orange)}
.brand-name{font-family:"Roboto",sans-serif;font-weight:700;font-size:34px;color:#d9d9d9;letter-spacing:1px}
.contact-strip{position:absolute;right:58px;top:20px;display:flex;gap:24px;font-size:15px;color:#bbb}
.contact-strip span{display:flex;align-items:center;gap:6px}
.main-nav{position:absolute;right:40px;top:56px;display:flex}
.main-nav a{display:block;height:52px;line-height:52px;padding:0 18px;color:#eee;font-size:17px;text-decoration:none}
.main-nav a.active{background:var(--orange);color:var(--white);border-radius:3px 3px 0 0}

/* hero */
.hero{position:absolute;top:108px;left:0;width:1200px;height:567px;
  background:linear-gradient(90deg,#1e1a17 0%,#3a302a 45%,#8a7c70 75%,#6b5d52 100%)}
.hero-title{position:absolute;left:58px;top:112px;width:700px;font-family:"Roboto Condensed",sans-serif;font-weight:700;font-size:47px;line-height:57px;color:var(--white);text-transform:uppercase}
.hero-text{position:absolute;left:58px;top:290px;width:590px;font-size:21px;line-height:32px;color:var(--white)}
.btn{display:inline-block;background:var(--orange);color:var(--white);border-radius:5px;text-decoration:none}
.hero .btn{position:absolute;left:58px;top:384px;padding:10px 14px;font-size:17px}

/* section headings */
.section-title{text-align:center;font-weight:700;font-size:31px;color:var(--ink)}
.divider{position:relative;width:200px;height:14px;margin:10px auto 0}
.divider::before{content:"";position:absolute;left:0;right:0;top:6px;height:2px;background:#333}
.divider::after{content:"";position:absolute;left:93px;top:0;width:14px;height:14px;background:#111}

/* what we do */
.what-we-do{position:absolute;top:675px;left:0;width:1200px;height:395px}
.what-we-do .section-title{margin-top:40px}
.services{position:absolute;left:59px;top:110px;display:flex;gap:32px}
.service-card{position:relative;width:244px;height:240px}
.service-card .panel{position:absolute;left:32px;top:48px;width:212px;height:192px;border:2px solid #444;border-radius:12px;background:var(--white)}
.service-card.featured .panel{border-color:var(--orange)}
.service-card .icon{position:absolute;left:0;top:0;width:112px;height:112px;background:#3d3d3d;border-radius:14px}
.service-card.featured .icon{background:var(--orange)}
.service-card .icon svg{position:absolute;left:26px;top:24px}
.service-card h3{position:absolute;left:132px;top:58px;width:110px;font-weight:500;font-size:16px;line-height:18px;color:var(--ink)}
.service-card p{position:absolute;left:48px;top:130px;width:186px;font-size:13px;line-height:23px;color:var(--text)}

/* IT support */
.it-support{position:absolute;top:1070px;left:0;width:1200px;height:508px;background:var(--grey-bg)}
.it-support .photo{position:absolute;left:0;top:0;width:520px;height:508px;
  background:linear-gradient(90deg,#3b3430 0%,#7a6a5e 55%,#d8d2cc 90%,var(--grey-bg) 100%)}
.it-support .section-title{position:absolute;left:540px;width:660px;top:38px}
.it-support .divider{position:absolute;left:770px;top:96px;margin:0}
.support-grid{position:absolute;left:548px;top:118px;display:grid;grid-template-columns:330px 300px;row-gap:20px;column-gap:18px}
.support-item{display:flex;gap:16px;height:72px}
.support-item .badge{flex:none;width:70px;height:70px;border-radius:50%;border:2px solid #333;background:var(--white);display:flex;align-items:center;justify-content:center}
.support-item.featured .badge{background:var(--orange);border-color:var(--orange)}
.support-item h4{font-weight:400;font-size:17px;color:var(--ink);margin-top:8px}
.support-item.featured h4{color:var(--orange)}
.support-item p{font-size:13px;line-height:19px;color:var(--muted)}

/* about */
.about{position:absolute;top:1578px;left:0;width:1200px;height:464px}
.about .section-title{position:absolute;left:0;width:1190px;top:42px}
.about .divider{position:absolute;left:500px;top:92px;margin:0}
.about-copy{position:absolute;left:59px;top:116px;width:670px;font-size:13.5px;line-height:26px;color:var(--muted)}
.about-copy p{margin-bottom:10px}
.about-copy strong{font-weight:500;color:var(--ink)}
.about .btn{position:absolute;left:59px;top:382px;padding:8px 14px;font-size:14px}
.about .photo{position:absolute;left:724px;top:40px;width:476px;height:380px;
  background:radial-gradient(ellipse at 60% 50%,#b9b3ad 0%,#e7e4e1 55%,var(--white) 80%)}

/* testimonials */
.testimonials{position:absolute;top:2042px;left:0;width:1200px;height:450px;
  background:linear-gradient(180deg,#141414 0%,#262626 50%,#151515 100%)}
.testimonials .section-title{position:absolute;width:1200px;top:40px;color:var(--white)}
.testimonials .divider{position:absolute;left:500px;top:90px;margin:0}
.testimonials .divider::before{background:#ccc}
.testimonials .divider::after{background:var(--white)}
.quote-mark{position:absolute;width:1200px;text-align:center;color:#ddd;font-family:Georgia,serif;font-size:60px;line-height:60px}
.quote-text{position:absolute;left:110px;top:192px;width:980px;text-align:center;font-size:16.5px;line-height:28px;color:#ddd}
.quote-author{position:absolute;top:338px;width:1200px;text-align:center;font-weight:500;font-size:18px;color:var(--white)}
.quote-author span{color:var(--orange)}
.quote-dots{position:absolute;top:382px;left:568px;display:flex;gap:8px}
.quote-dots i{width:10px;height:10px;border:2px solid var(--orange);transform:rotate(45deg)}

/* contact */
.contact{position:absolute;top:2492px;left:0;width:1200px;height:264px}
.contact .section-title{position:absolute;width:1200px;top:42px}
.contact .divider{position:absolute;left:500px;top:92px;margin:0}
.field{position:absolute;height:43px;border:1px solid #aaa;padding:12px 14px;font-size:13px;color:var(--muted);background:var(--white)}
.submit{position:absolute;left:965px;top:130px;width:102px;height:104px;background:var(--orange);border:1px solid var(--orange-dark);color:var(--white);font-weight:700;font-size:19px;display:flex;align-items:center;justify-content:center}

/* footer */
.site-footer{position:absolute;top:2756px;left:0;width:1200px;height:180px;background:var(--black);text-align:center}
.social{position:absolute;left:495px;top:48px;display:flex;gap:9px}
.social i{width:29px;height:29px;background:var(--orange);border-radius:2px}
.social i:nth-child(n+2){background:#bbb}
.footer-nav{position:absolute;top:94px;width:1200px;font-size:13px;color:#ccc}
.footer-nav a{color:#ccc;text-decoration:none}
.footer-nav a.active{color:var(--white)}
.copyright{position:absolute;top:120px;width:1200px;font-size:13px;color:#ccc}
</style>
</head>
<body>

<header class="site-header">
  <div class="brand"><span class="brand-mark"></span><span class="brand-name">VELMARKETA</span></div>
  <div class="contact-strip">
    <span><svg width="16" height="12" viewBox="0 0 16 12"><rect x="0.5" y="0.5" width="15" height="11" fill="#f58220"/><path d="M1 1l7 6 7-6" stroke="#0d0d0d" fill="none"/></svg>info@velmarketa.com</span>
    <span><svg width="14" height="14" viewBox="0 0 14 14"><path d="M3 1l3 3-2 2a8 8 0 0 0 4 4l2-2 3 3-2 2C6 13 1 8 1 3z" fill="#f58220"/></svg>+1 555.014.2287</span>
  </div>
  <nav class="main-nav">
    <a class="active" href="#">Home</a><a href="#">About</a><a href="#">Supports</a><a href="#">Clients</a><a href="#">Projects</a><a href="#">Careers</a><a href="#">Contact</a>
  </nav>
</header>

<section class="hero" role="img" aria-label="Photo of a smiling businesswoman working at a laptop in an office">
  <h1 class="hero-title">IT Solutions that work for your business a full service technology company</h1>
  <p class="hero-text">Outsourcing is subcontracting a process, such as product design or manufacturing, to a third-party company.</p>
  <a class="btn" href="#">Read More</a>
</section>

<section class="what-we-do">
  <h2 class="section-title">WHAT WE &nbsp;DO</h2>
  <div class="divider"></div>
  <div class="services">
    <article class="service-card featured">
      <div class="panel"></div>
      <div class="icon"><svg width="60" height="60" viewBox="0 0 60 60"><circle cx="22" cy="24" r="14" fill="none" stroke="#fff" stroke-width="7" stroke-dasharray="5 4"/><circle cx="22" cy="24" r="6" fill="#fff"/><circle cx="46" cy="44" r="8" fill="none" stroke="#fff" stroke-width="5" stroke-dasharray="3 3"/></svg></div>
      <h3>Managed IT Solutions</h3>
      <p>Our staff will design, service, administer and maintain your IT needs. We are well versed on all major operating…</p>
    </article>
    <article class="service-card">
      <div class="panel"></div>
      <div class="icon"><svg width="60" height="60" viewBox="0 0 60 60"><circle cx="26" cy="16" r="11" fill="#fff"/><path d="M6 56c0-16 8-24 20-24s20 8 20 24z" fill="#fff"/><rect x="34" y="34" width="24" height="16" fill="#3d3d3d" stroke="#fff" stroke-width="3"/></svg></div>
      <h3>Remote Diagnostic &amp; Support</h3>
      <p>Do you need a quick solution to a technical problem? With our live remote-assistance tool…</p>
    </article>
    <article class="service-card">
      <div class="panel"></div>
      <div class="icon"><svg width="60" height="60" viewBox="0 0 60 60"><rect x="4" y="6" width="52" height="36" rx="3" fill="none" stroke="#fff" stroke-width="4"/><rect x="12" y="14" width="20" height="5" fill="#fff"/><rect x="12" y="24" width="20" height="5" fill="#fff"/><rect x="20" y="48" width="20" height="5" fill="#fff"/></svg></div>
      <h3>Hosting and Virtulization</h3>
      <p>Lorem ipsum dolor sitet, consectetur adipiscing elit. Quisque pulvinar pretium interdumuisque coallis…</p>
    </article>
    <article class="service-card">
      <div class="panel"></div>
      <div class="icon"><svg width="60" height="60" viewBox="0 0 60 60"><rect x="6" y="12" width="48" height="32" fill="none" stroke="#fff" stroke-width="4"/><path d="M18 38l20-20 4 4-20 20h-4z" fill="#fff"/><rect x="18" y="48" width="24" height="5" fill="#fff"/></svg></div>
      <h3>IT Infrastructure Design &amp; Installation</h3>
      <p>Do you need a quick solution to a technical problem? With our live remote-assistance tool, a member of our support…</p>
    </article>
  </div>
</section>

<section class="it-support">
  <div class="photo" role="img" aria-label="Photo of a man working on a laptop at a desk"></div>
  <h2 class="section-title">IT SUPPORT SOLUTIONS</h2>
  <div class="divider"></div>
  <div class="support-grid">
    <div class="support-item featured"><span class="badge"><svg width="34" height="34" viewBox="0 0 34 34" stroke="#fff" stroke-width="2" fill="#fff"><circle cx="17" cy="17" r="4"/><circle cx="17" cy="4" r="3"/><circle cx="5" cy="26" r="3"/><circle cx="29" cy="26" r="3"/><path d="M17 7v6M8 24l6-4M26 24l-6-4"/></svg></span><div><h4>Network Adminstration</h4><p>risus nec commodo porttitor, arcu ipsum imperdiet lacus,</p></div></div>
    <div class="support-item"><span class="badge"><svg width="30" height="30" viewBox="0 0 30 30" fill="none" stroke="#333" stroke-width="2.5"><rect x="4" y="3" width="14" height="24" rx="2"/><rect x="20" y="10" width="7" height="17"/></svg></span><div><h4>Desktop Support</h4><p>Praesent consecteturant siut neque luctusnec luc</p></div></div>
    <div class="support-item"><span class="badge"><svg width="30" height="30" viewBox="0 0 30 30" fill="none" stroke="#333" stroke-width="2.5"><rect x="5" y="3" width="8" height="8"/><rect x="17" y="3" width="8" height="8"/><path d="M9 11v8a6 6 0 0 0 12 0v-8M15 25v4"/></svg></span><div><h4>Netwrok Cabling</h4><p>Asrit consectetur tellus nunc vitae lacusliquam phare</p></div></div>
    <div class="support-item"><span class="badge"><svg width="30" height="30" viewBox="0 0 30 30" fill="none" stroke="#333" stroke-width="2.5"><path d="M3 11a17 17 0 0 1 24 0M7 16a11 11 0 0 1 16 0M11 21a5 5 0 0 1 8 0"/><circle cx="15" cy="25" r="1.5" fill="#333"/></svg></span><div><h4>Wireless Network</h4><p>Tus massa pulvinaraece nasnisl neque elementu</p></div></div>
    <div class="support-item"><span class="badge"><svg width="30" height="30" viewBox="0 0 30 30" fill="#333"><rect x="3" y="8" width="24" height="18" rx="2"/><rect x="8" y="3" width="14" height="6"/><rect x="7" y="12" width="4" height="3" fill="#fff"/><rect x="13" y="12" width="4" height="3" fill="#fff"/><rect x="19" y="12" width="4" height="3" fill="#fff"/></svg></span><div><h4>Telecommunications</h4><p>tra nisi enim, vitae interdum nisl euismod eusuce utneque</p></div></div>
    <div class="support-item"><span class="badge"><svg width="28" height="30" viewBox="0 0 28 30"><path d="M14 2l11 4v9c0 7-5 11-11 13C8 26 3 22 3 15V6z" fill="#333"/><path d="M14 6v18" stroke="#fff" stroke-width="2"/></svg></span><div><h4>Antivirus Soultions</h4><p>Smet massa euursus vrr ipsum Vivamus vehicula</p></div></div>
    <div class="support-item"><span class="badge"><svg width="30" height="30" viewBox="0 0 30 30" fill="none" stroke="#333" stroke-width="2.5"><circle cx="15" cy="15" r="11"/><circle cx="15" cy="15" r="5"/><path d="M7 7l4 4M23 7l-4 4M7 23l4-4M23 23l-4-4"/></svg></span><div><h4>Disaster Recovery</h4><p>ipsum. Vestibulum a augue nisi. Nulla luctus leo mi,</p></div></div>
    <div class="support-item"><span class="badge"><svg width="30" height="30" viewBox="0 0 30 30" fill="none" stroke="#333" stroke-width="2.5"><rect x="3" y="5" width="24" height="16"/><path d="M11 26h8M15 21v5M8 10h8M8 14h12"/></svg></span><div><h4>Web Design</h4><p>Bibendum augue ac laci sagittis accums pulvinar</p></div></div>
  </div>
</section>

<section class="about">
  <h2 class="section-title">ABOUT US</h2>
  <div class="divider"></div>
  <div class="about-copy">
    <p><strong>Outsourcing</strong> is subcontracting a process, such as product design or manufacturing, to a third-party company. The decision to outsource is often made in the interest of lowering firm costs, redirecting or conserving energy directed at the competencies of a particular business, or to make more efficient use of land, labor, capital, (information) technology and resources. &nbsp;&nbsp;Outsourcing became part of the business lexicon during the 1980s.</p>
    <p>Velmarketa is a technology solution provider based in Houston, Texas. Our goal is to make technology a non-issue for individuals and small to medium size businesses ranging from 5 to 150 Users. Velmarketa has the experience, the tools, high-level technology solutions and training to power your business and your work force. We understand that all business's have one goal in common!</p>
  </div>
  <a class="btn" href="#">Read More</a>
  <div class="photo" role="img" aria-label="Photo of a businesswoman holding a cup beside a laptop"></div>
</section>

<section class="testimonials" role="img" aria-label="Dark background photo of an office team meeting">
  <h2 class="section-title">TESTIMONIALS</h2>
  <div class="divider"></div>
  <div class="quote-mark" style="top:130px">“</div>
  <p class="quote-text">We are extremely happy with our frank, open, and honest relationship with Brightline Partners. Brightline Partners' solution and delivery capabilities in the technology business not only improved the time to market and predictability, but reduced the cost of implementation</p>
  <div class="quote-mark" style="top:270px">”</div>
  <p class="quote-author">Lorem ipsum <span>|</span> Company Name</p>
  <div class="quote-dots"><i></i><i></i><i></i><i></i></div>
</section>

<section class="contact">
  <h2 class="section-title">CONTACT US</h2>
  <div class="divider"></div>
  <div class="field" style="left:137px;top:130px;width:254px">First Name:</div>
  <div class="field" style="left:407px;top:130px;width:253px">Last Name:</div>
  <div class="field" style="left:137px;top:191px;width:254px">Phone:</div>
  <div class="field" style="left:407px;top:191px;width:253px">Email:</div>
  <div class="field" style="left:675px;top:130px;width:274px;height:104px">Comments:</div>
  <div class="submit">SUBMIT</div>
</section>

<footer class="site-footer">
  <div class="social"><i></i><i></i><i></i><i></i><i></i><i></i></div>
  <div class="footer-nav"><a class="active" href="#">Home</a> &nbsp;/&nbsp; <a href="#">About Us</a> &nbsp;/&nbsp; <a href="#">Supports</a> &nbsp;/&nbsp; <a href="#">Client</a> &nbsp;/&nbsp; <a href="#">Careers</a> &nbsp;/&nbsp; <a href="#">Contact</a></div>
  <div class="copyright">© 2017. velmarketa.All Rights Reserved.</div>
</footer>

</body>
</html>
```